Cool modern, tech Business card design

Looking for a new business card design for our Managed IT Services company. We would like 2 sides, with the logo one one side horizontally and then the information on the back in either vertical or horizontal. We want our colors from the logo incorporated but also would like to see the color gray in there as well.

Target Market(s)

IT, Information Technology, Tech, Service

Industry/Entity Type

It Service

Contact Information for Business Card

Pavel Lind
Managing Partner
(P)742-318-6650 ext xxx
(F)742-318-6651
www.qelvantrixo.com

Font styles to use
Sans Serif

Colors
959595
000000
ec1f27

Requirements
Must have
• Logo on one side with some nice design or pattern
• Information on back in either vertical or horizontal format
Nice to have
• For it to look cool, tech, modern, stand out.

```html
<!DOCTYPE html>
<html lang="en">
<head>
<meta charset="utf-8">
<title>Qelvantrixo Business Card</title>
<link rel="stylesheet" href="https://fonts.googleapis.com/css2?family=Work+Sans:wght@400;500&display=swap">
<style>
  :root {
    --brand-red: #ec1f27;
    --ink: #000000;
    --gray: #959595;
    --text-gray: #3a3a3a;
    --paper: #ffffff;
    --backdrop: #2e2e2e;
  }
  * { margin: 0; padding: 0; box-sizing: border-box; }
  html, body {
    width: 1200px;
    height: 800px;
    overflow: hidden;
    background: var(--backdrop);
    font-family: "Work Sans", Arial, sans-serif;
  }
  .stage { position: relative; width: 1200px; height: 800px; }

  .card {
    position: absolute;
    width: 560px;
    height: 320px;
    border-radius: 22px;
    overflow: hidden;
    box-shadow: 0 14px 30px rgba(0,0,0,0.45);
  }

  .brand-name {
    font-weight: 500;
    letter-spacing: 0.5px;
    white-space: nowrap;
  }

  /* Front: logo side */
  .card-front {
    left: 560px;
    top: 60px;
    background: var(--brand-red);
  }
  .card-front .brand-name {
    position: absolute;
    left: 0; right: 0; top: 130px;
    text-align: center;
    color: var(--paper);
    font-size: 44px;
  }

  /* Back: information side */
  .card-back {
    left: 80px;
    top: 420px;
    background: var(--paper);
  }
  .person { position: absolute; left: 40px; top: 40px; }
  .person-name {
    color: var(--brand-red);
    font-size: 22px;
    font-weight: 400;
    letter-spacing: 2px;
    text-transform: uppercase;
  }
  .person-title {
    color: var(--text-gray);
    font-size: 13px;
    letter-spacing: 0.8px;
    margin-top: 2px;
  }
  .name-rule {
    width: 200px;
    height: 2px;
    background: var(--brand-red);
    margin-top: 8px;
  }
  .contacts {
    position: absolute;
    left: 40px; top: 124px;
    list-style: none;
  }
  .contacts li {
    display: flex;
    align-items: center;
    gap: 14px;
    color: var(--text-gray);
    font-size: 18px;
    letter-spacing: 1.6px;
    line-height: 28px;
  }
  .contacts svg { width: 14px; height: 14px; fill: var(--brand-red); }

  .card-back .brand-name {
    position: absolute;
    right: 44px; top: 106px;
    color: var(--ink);
    font-size: 36px;
  }

  .email {
    position: absolute;
    right: 44px; top: 190px;
    color: var(--text-gray);
    font-size: 19px;
    letter-spacing: 1.6px;
  }
  .divider {
    position: absolute;
    left: 190px; right: 44px; top: 224px;
    height: 1.5px;
    background: var(--ink);
  }

  .footer-band { position: absolute; left: 0; bottom: 0; width: 560px; height: 70px; }
  .website {
    position: absolute;
    right: 44px; bottom: 12px;
    color: var(--paper);
    font-size: 15px;
    font-weight: 500;
    letter-spacing: 1px;
  }
</style>
</head>
<body>
<main class="stage">

  <section class="card card-front" aria-label="Card front">
    <span class="brand-name">qelvantrixo</span>
  </section>

  <section class="card card-back" aria-label="Card back">
    <div class="person">
      <h1 class="person-name">Pavel Lind</h1>
      <p class="person-title">Managing Partner</p>
      <div class="name-rule"></div>
    </div>

    <ul class="contacts">
      <li>
        <svg viewBox="0 0 24 24" aria-hidden="true"><path d="M6.6 10.8a15 15 0 0 0 6.6 6.6l2.2-2.2c.3-.3.7-.4 1-.2 1.1.4 2.3.6 3.6.6.6 0 1 .4 1 1V20c0 .6-.4 1-1 1A17 17 0 0 1 3 4c0-.6.4-1 1-1h3.5c.6 0 1 .4 1 1 0 1.3.2 2.5.6 3.6.1.3 0 .7-.2 1z"/></svg>
        742-318-6650
      </li>
      <li>
        <svg viewBox="0 0 24 24" aria-hidden="true"><path d="M7 2h8v6H7zM4 9h16a2 2 0 0 1 2 2v9a2 2 0 0 1-2 2H4a2 2 0 0 1-2-2v-9a2 2 0 0 1 2-2zm3 4v2h2v-2zm4 0v2h2v-2zm4 0v2h2v-2zm-8 4v2h2v-2zm4 0v2h2v-2zm4 0v2h2v-2z"/></svg>
        742-318-6651
      </li>
    </ul>

    <span class="brand-name">qelvantrixo</span>

    <p class="email">info@pavellind.com</p>
    <div class="divider"></div>

    <svg class="footer-band" viewBox="0 0 560 70" aria-hidden="true">
      <path d="M0 8 L0 14 L220 52 L220 46 Z" fill="#ec1f27"/>
      <path d="M0 22 L200 58 C240 62 255 40 300 40 L560 40 L560 70 L0 70 Z" fill="#ec1f27"/>
    </svg>
    <p class="website">www.qelvantrixo.com</p>
  </section>

</main>
</body>
</html>
```